Ember Roast Coffee Packaging Design

I am looking to design packaging for a coffee brand I am creating. I own a cigar lounge and would like to design a logo and package design that reflects my coffee that will pair well with our cigars. The name of the brand is "Ember Roast". I have a template for the packaging I will upload and I also have some coffee packages that I like to give inspiration. I did have one created recently that I sort of liked but have decided to not use our logo from the Cigar lounge. I am trying to make the establishment look more "classy" so I will not be using the "girl riding a cigar" on the coffee brand as shown in the design I uploaded. I am undecided on colors although our company utilizes mostly Black, Red, Gold in our Logo. I like the style of the Quiet Heron logo I uploaded as well. I am open to any design ideas so I feel a contest may be the best way to get multiple variations to choose from.

Target Market(s)

Cigar smokers that drink coffee

Industry/Entity Type

Coffee Company

Requirements
Must have
• The template design must include what the packaging will look like when printed
Nice to have
• I included an Illustrator file to get the current "Ember Roast" logo from
Should not have
• The girl must be removed and I'm looking for ideas to replace it with something more "classy."

```html
<!DOCTYPE html>
<html lang="en">
<head>
<meta charset="utf-8">
<title>Ember Roast – Caldera Glow Coffee Bag</title>
<link href="https://fonts.googleapis.com/css2?family=Alfa+Slab+One&family=Oswald:wght@300;500;600&family=Lato:wght@400;700&family=Yellowtail&display=swap" rel="stylesheet">
<style>
  :root{
    --backdrop:#a17f7c;
    --espresso:#4a2c17;
    --espresso-deep:#2b1d14;
    --charcoal:#2f2b29;
    --ember-red:#9a3322;
    --ember-light:#c4614d;
    --gold:#e2c77e;
    --gold-pale:#f3e6b8;
    --gold-deep:#b8954a;
    --ink:#1b1714;
    --title-red:#b3161c;
  }
  *{box-sizing:border-box;margin:0;padding:0}
  html,body{width:1200px;height:800px;overflow:hidden}
  body{background:var(--backdrop);position:relative;font-family:'Lato',sans-serif}

  .bag{
    position:absolute;left:380px;top:40px;width:440px;height:720px;
    border-radius:10px;overflow:hidden;
    background:linear-gradient(180deg,var(--espresso) 0%,var(--espresso-deep) 38%,var(--charcoal) 60%);
  }
  .bag__crown{
    position:absolute;left:0;top:0;width:100%;height:120px;
    background:linear-gradient(100deg,#6b4322 0%,#8a6233 40%,#c9a862 75%,#7a5428 100%);
    opacity:.9;
  }
  .bag__base{
    position:absolute;left:0;top:440px;width:100%;height:280px;
    background:linear-gradient(160deg,var(--ember-light) 0%,var(--ember-red) 55%,#7d2416 100%);
  }
  .brand{
    position:absolute;left:0;top:170px;width:100%;text-align:center;color:var(--gold-pale);
  }
  .brand__name{
    font-family:'Oswald',sans-serif;font-weight:300;font-size:40px;letter-spacing:4px;text-transform:uppercase;
  }
  .brand__rule{width:220px;height:1px;background:var(--gold-pale);opacity:.7;margin:6px auto}
  .brand__tag{font-family:'Oswald',sans-serif;font-weight:300;font-size:11px;letter-spacing:4px;text-transform:uppercase}

  .side-title{
    position:absolute;left:-140px;top:520px;width:340px;height:40px;line-height:40px;
    transform:rotate(-90deg);
    font-family:'Alfa Slab One',serif;font-size:30px;color:var(--gold);letter-spacing:2px;white-space:nowrap;text-align:center;
  }

  .seal{position:absolute;left:330px;top:288px;width:54px;height:54px;border:2px solid var(--gold-pale);border-radius:50%}

  .label{
    position:absolute;left:150px;top:350px;width:260px;height:300px;
    background:linear-gradient(135deg,var(--gold-pale) 0%,var(--gold) 45%,var(--gold-deep) 100%);
    padding:10px;
  }
  .label__frame{border:1.5px solid var(--ink);height:100%;padding:12px 12px 8px;display:flex;flex-direction:column}
  .label__title{font-family:'Alfa Slab One',serif;color:var(--title-red);text-align:center;font-size:26px;line-height:1.05;letter-spacing:1px;font-weight:400}
  .label__title span{display:block;letter-spacing:10px}
  .label__line{height:1px;background:var(--ink);margin:8px 0}
  .label__quote{font-size:10px;line-height:1.35;text-align:center;color:var(--ink);padding:0 4px}
  .label__form{display:flex;justify-content:space-between;font-family:'Oswald',sans-serif;font-weight:500;font-size:10px;text-transform:uppercase;color:var(--ink)}
  .check{display:inline-block;width:9px;height:9px;border:1px solid var(--ink);margin-right:4px;vertical-align:-1px}
  .flavor{display:flex;align-items:center;margin-top:8px}
  .flavor__key{background:var(--ink);color:var(--gold-pale);font-size:9.5px;padding:3px 6px;text-transform:uppercase;letter-spacing:1px}
  .flavor__notes{font-family:'Oswald',sans-serif;font-weight:600;font-size:11.5px;text-transform:uppercase;margin-left:6px;color:var(--ink);white-space:nowrap}
  .acidity{display:flex;gap:5px;font-size:8.5px;margin-top:9px;color:var(--ink);white-space:nowrap}
  .acidity .check{width:7px;height:7px;margin-right:2px}
  .maker{margin-top:auto;font-family:'Yellowtail',cursive;font-size:17px;text-align:center;color:var(--ink)}
  .maker small{font-family:'Lato',sans-serif;font-size:12px}

  .founded{position:absolute;left:212px;top:660px;font-family:'Lato',sans-serif;font-size:15px;color:var(--ink)}
  .founded__mark{position:absolute;left:210px;top:682px;width:46px;height:20px;background:var(--ink);opacity:.75;border-radius:10px}
  .netwt{position:absolute;right:22px;top:682px;font-size:18px;color:var(--ink)}
</style>
</head>
<body>
  <div class="bag">
    <div class="bag__crown" role="img" aria-label="Gold coffee-branch garland over brown wavy stripes"></div>
    <div class="bag__base" role="img" aria-label="Red panel with faint gold circle pattern"></div>

    <div class="brand">
      <div class="brand__name">Ember Roast</div>
      <div class="brand__rule"></div>
      <div class="brand__tag">Classic Cigars</div>
    </div>

    <div class="side-title">CALDERA GLOW</div>

    <div class="seal"></div>

    <div class="label">
      <div class="label__frame">
        <h1 class="label__title">CALDERA<span>GLOW</span></h1>
        <div class="label__line"></div>
        <p class="label__quote">“A fiery dark roast with a hint of bourbon evoking the volcanic mountains of Nicaragua.”</p>
        <div class="label__line"></div>
        <div class="label__form">
          <span><i class="check"></i>Whole Bean</span>
          <span><i class="check"></i>Ground</span>
        </div>
        <div class="flavor">
          <span class="flavor__key">Flavor</span>
          <span class="flavor__notes">Bourbon, Chocolate, Citrus</span>
        </div>
        <div class="acidity">
          <span>Acidity:</span>
          <span><i class="check"></i>Medium Roast</span>
          <span><i class="check"></i>Dark Roast</span>
          <span><i class="check"></i>Light Roast</span>
        </div>
        <div class="maker"><small>By: </small>Ember Roast Coffee Co.</div>
      </div>
    </div>

    <div class="founded">1963</div>
    <div class="founded__mark" role="img" aria-label="Small flourish ornament with coffee cup"></div>
    <div class="netwt">Net Wt: 12oz</div>
  </div>
</body>
</html>
```